PLOVEN Business Card

Coastal Build Additions and Refits. I need a business card designed for this new high end renovation business. I would like the logo centered on the back side with the ABN (37 915 402 176) on the bottom right hand corner.

I would like the following information placed on the other side along with some customized pattern or design.

Derek Collwood
Director
Phone: 1300 480 957
Fax: (02) 8145 9021
Website: www.plovenbuilders.com.au
Email: d.collwood@plovenbuilders.com.au
PO Box 87,
Kelvinbrook NSW 2069

(FB Logo) PLOVEN - Coastal Build Additions and Refits

The final design should communicate professionalism and trust.

Back side background colour: white
Front side: Undecided

```html
<!DOCTYPE html>
<html lang="en">
<head>
<meta charset="UTF-8">
<title>PLOVEN Business Card</title>
<link rel="stylesheet" href="https://fonts.googleapis.com/css2?family=Cinzel:wght@600&family=Arimo:wght@400;700&display=swap">
<style>
  :root {
    --stage: #2b2b2d;
    --card: #ffffff;
    --ink: #2a2a2a;
    --brand-blue: #1f5b9e;
    --text-blue: #1e4f8c;
    --rule: #1f1f1f;
    --pattern-light: #f4f5f7;
    --pattern-mid: #e6e8ec;
  }
  * { margin: 0; padding: 0; box-sizing: border-box; }
  html, body { width: 1200px; height: 900px; overflow: hidden; }
  body { background: var(--stage); position: relative; font-family: "Arimo", Arial, sans-serif; }

  .card {
    position: absolute;
    left: 320px;
    width: 560px;
    height: 320px;
    background: var(--card);
    overflow: hidden;
  }
  .card--back { top: 90px; }
  .card--front { top: 490px; }

  .back-pattern {
    position: absolute; inset: 0;
    background: linear-gradient(135deg, var(--pattern-light), var(--pattern-mid) 50%, var(--pattern-light));
  }

  .logo { position: absolute; text-align: center; }
  .logo__name {
    display: block;
    font-family: "Cinzel", Georgia, serif;
    font-weight: 600;
    color: var(--ink);
    letter-spacing: 4px;
    line-height: 1;
  }
  .logo__tagline {
    display: flex; align-items: center; justify-content: center; gap: 8px;
    font-family: "Cinzel", Georgia, serif;
    font-weight: 600;
    color: var(--brand-blue);
    letter-spacing: 1px;
    white-space: nowrap;
  }
  .logo__tagline::before, .logo__tagline::after {
    content: ""; display: block; height: 1.5px; width: 34px; background: var(--brand-blue);
  }

  .card--back .logo { left: 0; right: 0; top: 104px; }
  .card--back .logo__name { font-size: 62px; }
  .card--back .logo__tagline { font-size: 13px; margin-top: 8px; }

  .abn {
    position: absolute; right: 26px; bottom: 22px;
    font-weight: 700; font-size: 14px; color: var(--ink);
  }

  .card--front .logo { left: 40px; width: 300px; top: 32px; }
  .card--front .logo__name { font-size: 48px; }
  .card--front .logo__tagline { font-size: 10px; margin-top: 7px; }

  .person { position: absolute; left: 40px; top: 196px; width: 230px; text-align: right; }
  .person__name { font-weight: 700; font-size: 21px; color: var(--text-blue); }
  .person__role { font-size: 14px; color: var(--text-blue); margin-top: 3px; }

  .divider {
    position: absolute; left: 292px; top: 138px; width: 2px; height: 160px; background: var(--rule);
  }

  .contact { position: absolute; left: 306px; top: 140px; list-style: none; }
  .contact__item {
    display: flex; align-items: center; gap: 8px;
    font-size: 13px; color: var(--text-blue); height: 21px; white-space: nowrap;
  }
  .contact__item--gap { margin-top: 8px; }
  .contact__icon { width: 13px; height: 13px; flex: none; fill: var(--ink); }
</style>
</head>
<body>

  <section class="card card--back" aria-label="Card back">
    <div class="back-pattern" role="img" aria-label="Faint repeated brand name pattern across the card"></div>
    <div class="logo">
      <span class="logo__name">PLOVEN</span>
      <span class="logo__tagline">Coastal Build Additions &amp; Refits</span>
    </div>
    <p class="abn">(ABN 37 915 402 176)</p>
  </section>

  <section class="card card--front" aria-label="Card front">
    <div class="logo">
      <span class="logo__name">PLOVEN</span>
      <span class="logo__tagline">Coastal Build Additions &amp; Refits</span>
    </div>

    <div class="person">
      <p class="person__name">Derek Collwood</p>
      <p class="person__role">Director</p>
    </div>

    <div class="divider"></div>

    <ul class="contact">
      <li class="contact__item">
        <svg class="contact__icon" viewBox="0 0 16 16"><path d="M2 6c0-2 3-3 6-3s6 1 6 3v1h-3V6H5v1H2z M4 8h8l1 5H3z"/></svg>
        1300 480 957
      </li>
      <li class="contact__item">
        <svg class="contact__icon" viewBox="0 0 16 16"><path d="M4 1h7v5H4z M1 7h14v8H1z"/></svg>
        (02) 8145 9021
      </li>
      <li class="contact__item contact__item--gap">
        <svg class="contact__icon" viewBox="0 0 16 16"><circle cx="8" cy="8" r="6.5" fill="none" stroke="#2a2a2a" stroke-width="1.5"/><path d="M1.5 8h13M8 1.5c-3 3-3 10 0 13M8 1.5c3 3 3 10 0 13" fill="none" stroke="#2a2a2a" stroke-width="1.2"/></svg>
        www.plovenbuilders.com.au
      </li>
      <li class="contact__item">
        <svg class="contact__icon" viewBox="0 0 16 16"><path d="M1 3h14v10H1z"/><path d="M1 3l7 6 7-6" fill="none" stroke="#fff" stroke-width="1.2"/></svg>
        d.collwood@plovenbuilders.com.au
      </li>
      <li class="contact__item">
        <svg class="contact__icon" viewBox="0 0 16 16"><path d="M8 1a5 5 0 0 1 5 5c0 4-5 9-5 9S3 10 3 6a5 5 0 0 1 5-5z"/><circle cx="8" cy="6" r="2" fill="#fff"/></svg>
        PO Box 87, Kelvinbrook NSW 2069
      </li>
      <li class="contact__item contact__item--gap">
        <svg class="contact__icon" viewBox="0 0 16 16"><circle cx="8" cy="8" r="4"/></svg>
        www.chatterpage.com/coastalrefits1
      </li>
    </ul>
  </section>

</body>
</html>
```